New For Sale Signs

We are looking for a design not too dissimilar to the attached. Looking more for tweaks than a radically new concept. The attached just isn't quite right. Looking to add a touch more grey (our secondary colour). We look forward to seeing your new designs!

Thank you so much for all of your creative input. We have now found the perfect design but very much appreciate your participation and wish you all the best. Kind regards, Rosalind Pemberly Brightwell Estate Agents

```html
<!DOCTYPE html>
<html lang="en">
<head>
<meta charset="utf-8">
<title>Brightwell Estate Agents – For Sale Sign</title>
<link rel="stylesheet" href="https://fonts.googleapis.com/css2?family=Inter:wght@300;400&display=swap">
<style>
  :root {
    --backdrop: #ecebe8;
    --sign-blue: #005a78;
    --brand-white: #ffffff;
    --secondary-grey: #a9b0b7;
    --rule-grey: #9aa6ae;
    --pattern-teal: #0a7690;
    --pattern-bright: #1a8fc8;
  }
  * { margin: 0; padding: 0; box-sizing: border-box; }
  html, body {
    width: 957px;
    height: 1200px;
    overflow: hidden;
    background: var(--backdrop);
    font-family: "Inter", Arial, sans-serif;
  }
  .canvas {
    position: relative;
    width: 957px;
    height: 1200px;
  }
  .sign {
    position: absolute;
    left: 143px;
    top: 97px;
    width: 670px;
    height: 1005px;
    background: var(--sign-blue);
    overflow: hidden;
    text-align: center;
  }
  .brand-name {
    position: absolute;
    left: 0;
    right: 0;
    top: 62px;
    color: var(--brand-white);
    font-weight: 400;
  }
  .brand-name__main {
    display: block;
    font-size: 78px;
    line-height: 1;
    letter-spacing: 6px;
  }
  .brand-name__sub {
    display: block;
    margin-top: 14px;
    font-size: 24px;
    line-height: 1;
    letter-spacing: 6px;
  }
  .rule {
    position: absolute;
    left: 42px;
    width: 586px;
    height: 2px;
    background: var(--rule-grey);
  }
  .rule--top { top: 250px; }
  .rule--bottom { top: 394px; }
  .headline {
    position: absolute;
    left: 0;
    right: 0;
    top: 252px;
    color: var(--secondary-grey);
    font-weight: 300;
    font-size: 138px;
    line-height: 140px;
    letter-spacing: 0;
  }
  .tagline {
    position: absolute;
    left: 0;
    right: 0;
    top: 400px;
    color: var(--secondary-grey);
    font-weight: 300;
    font-size: 70px;
    line-height: 84px;
    letter-spacing: -1px;
  }
  .call-note {
    position: absolute;
    left: 0;
    right: 0;
    top: 481px;
    color: var(--secondary-grey);
    font-size: 18.5px;
    line-height: 22px;
  }
  .phone {
    position: absolute;
    left: 0;
    right: 0;
    top: 500px;
    color: var(--brand-white);
    font-weight: 300;
    font-size: 106px;
    line-height: 116px;
    letter-spacing: 1px;
  }
  .website {
    position: absolute;
    left: 0;
    right: 0;
    top: 645px;
    color: var(--secondary-grey);
    font-weight: 300;
    font-size: 34px;
    line-height: 44px;
  }
  .pattern-band {
    position: absolute;
    left: 0;
    bottom: 0;
    width: 670px;
    height: 280px;
    background: linear-gradient(180deg, var(--sign-blue) 0%, var(--pattern-teal) 45%, var(--pattern-bright) 100%);
  }
</style>
</head>
<body>
  <div class="canvas">
    <section class="sign">
      <div class="brand-name">
        <span class="brand-name__main">BRIGHTWELL</span>
        <span class="brand-name__sub">ESTATE AGENTS</span>
      </div>
      <div class="rule rule--top"></div>
      <h1 class="headline">For Sale</h1>
      <div class="rule rule--bottom"></div>
      <p class="tagline">Moving.Forward.</p>
      <p class="call-note">For further information regarding this property please call</p>
      <p class="phone">4512 6040</p>
      <p class="website">brightwellestateagents.com.au</p>
      <div class="pattern-band" role="img" aria-label="Decorative pattern of overlapping translucent blue and teal hexagons"></div>
    </section>
  </div>
</body>
</html>
```